Pharmaceutical Manufacturing Services Advertisement

We need a new full page advertisement designed for publication in international magazines. We are a custom pharmaceutical manufacturing company and we help biotechnology companies scale up their drug development for clinical trials. The products we help manufacture are therapeutics for global healthcare problems.

Target Market(s)

Verott Bio is a privately owned contract development manufacturing organisation (CDMO) headquartered in Darra, QLD, Australia.

Our mission is to is to be a global leader in development and in the provision of contract manufacturing for active pharmaceutical ingredient processes.

Why we do what we Do:

To help advance Biotechnology Companies so that they can deliver innovative therapeutics
~ enabling patients to live longer, healthier and happier lives
~ which solves worldwide health problems

Verott Bio’s role is to develop, implement and scale up the production to deliver biologic medicines for patients in partnership with the biotechnology companies.

Industry/Entity Type

Biotechnology

Font styles to use
Sans Serif

Colors

Designer to choose colors to be used in the design.

Requirements
Must have
• Please see the script on the Word document. There are 4 optional Header Taglines. Additional ideas for multiple designs for the taglines welcomed.
• However preference is for either of the first two:
• 1. Building your vision for better healthcare
• 2. Bridging your vision for better healthcare
• File Specs:
• • All artwork should be submitted as high-resolution (300 min. dpi), press-ready PDF files
• • CMYK color only
• • Full page 8.25” x 10.812”; 209.55 x 274.62 mm
• • Live Area for all sizes: 0.25” (6.35 mm) inside the trim
• • Bleed Area for all sizes: Extends 0.125” (3.175 mm) from trim
Nice to have
• Modern Science look to inspire biotechnology companies to work with us.
• Search for images to use by keyword "recombinant dna"

```html
<!DOCTYPE html>
<html lang="en">
<head>
<meta charset="utf-8">
<title>Verott Bio – Bridging your Vision for Better Healthcare</title>
<link href="https://fonts.googleapis.com/css2?family=Raleway:wght@300&family=Mulish:wght@400;500&family=Rubik:wght@400;500;700&display=swap" rel="stylesheet">
<style>
  :root {
    --navy: #173a5e;
    --lime: #a9c03a;
    --lime-soft: #b3c845;
    --white: #ffffff;
    --grey-text: #4a5563;
    --sea-1: #2a7d9c;
    --sea-2: #6aaec6;
    --mist: #c9d6de;
  }
  * { margin: 0; padding: 0; box-sizing: border-box; }
  html, body { width: 943px; height: 1200px; overflow: hidden; background: var(--white); }
  .ad {
    position: relative;
    width: 943px;
    height: 1200px;
    overflow: hidden;
    background: var(--white);
    font-family: "Mulish", sans-serif;
    color: var(--navy);
  }
  .hero-photo {
    position: absolute;
    left: 0; top: 0;
    width: 943px; height: 930px;
    background:
      radial-gradient(ellipse at 78% 40%, #d9dfe3 0%, rgba(217,223,227,0) 38%),
      radial-gradient(ellipse at 18% 78%, #9fb8d2 0%, rgba(159,184,210,0) 45%),
      linear-gradient(180deg, #8fc1d4 0%, var(--sea-2) 10%, var(--sea-1) 30%, #4f95ae 48%, var(--mist) 75%, var(--white) 100%);
  }
  .headline-band {
    position: absolute;
    left: 255px; top: 475px;
    width: 688px; height: 138px;
    background: var(--lime);
  }
  .headline {
    position: absolute;
    left: 52px; top: 12px;
    font-family: "Raleway", sans-serif;
    font-weight: 300;
    font-size: 55px;
    line-height: 60px;
    color: var(--white);
    letter-spacing: 0.2px;
    white-space: nowrap;
  }
  .intro-panel {
    position: absolute;
    left: 255px; top: 613px;
    width: 688px; height: 297px;
    background: var(--navy);
    color: var(--white);
    padding: 24px 0 0 52px;
  }
  .intro-title {
    font-family: "Rubik", sans-serif;
    font-weight: 700;
    font-size: 18.5px;
    margin-bottom: 12px;
    white-space: nowrap;
  }
  .intro-text {
    width: 560px;
    font-size: 15.8px;
    line-height: 24.7px;
    margin-bottom: 18px;
  }
  .list-label {
    position: absolute;
    height: 25px;
    padding: 0 26px 0 14px;
    font-family: "Rubik", sans-serif;
    font-weight: 700;
    font-size: 18px;
    line-height: 25px;
    color: var(--navy);
    background: linear-gradient(105deg, var(--lime-soft) 86%, transparent 86.5%);
  }
  .services-label { left: 62px; top: 932px; }
  .products-label { left: 347px; top: 957px; }
  .offer-list {
    position: absolute;
    list-style: none;
    font-family: "Rubik", sans-serif;
    font-size: 15.6px;
    line-height: 22px;
    color: var(--navy);
    white-space: nowrap;
  }
  .offer-list li { position: relative; padding-left: 15px; }
  .offer-list li::before {
    content: "·";
    position: absolute; left: 0; top: 0;
  }
  .services-list { left: 62px; top: 964px; }
  .products-list { left: 347px; top: 1000px; }
  .brand {
    position: absolute;
    left: 572px; top: 1022px;
    width: 300px;
    white-space: nowrap;
  }
  .brand-name {
    display: flex; align-items: center; gap: 10px;
    font-family: "Rubik", sans-serif;
    font-weight: 500;
    font-size: 40px;
    line-height: 48px;
    color: var(--navy);
    letter-spacing: 1px;
  }
  .brand-dot {
    width: 14px; height: 14px; border-radius: 50%;
    background: var(--lime);
  }
  .brand-tagline {
    margin-top: 6px;
    font-family: "Rubik", sans-serif;
    font-size: 14px;
    line-height: 18px;
    color: var(--grey-text);
  }
  .footer-rule {
    position: absolute;
    left: 62px; top: 1118px;
    width: 802px; height: 2px;
    background: var(--lime);
  }
  .contact-line {
    position: absolute;
    left: 68px; top: 1128px;
    font-family: "Rubik", sans-serif;
    font-size: 19.5px;
    line-height: 26px;
    color: var(--navy);
    white-space: nowrap;
  }
  .contact-line strong { font-weight: 700; }
  .contact-line span { margin-left: 12px; }
</style>
</head>
<body>
<main class="ad">
  <div class="hero-photo" role="img" aria-label="Photo collage: coastal bridge curving over the sea, lab technicians at a stainless fermentation vessel, and a blue DNA double helix"></div>

  <section class="headline-band">
    <h1 class="headline">Bridging your Vision<br>for Better Healthcare</h1>
  </section>

  <section class="intro-panel">
    <h2 class="intro-title">Your Partner in Early Phase Clinical Biomanufacturing</h2>
    <p class="intro-text">We have been serving the pharmaceutical, biotechnology and veterinary industry for over 20 years so you can create innovative medicines for worldwide health problems.</p>
    <p class="intro-text">Get your therapeutics to the patient faster with cost-effective manufacturing for your GMP clinical trial material. We offer rapid technology transfer, scale-up development and manufacturing of microbial cell-derived proteins at up to 500L scale. We prepare your active pharmaceutical ingredient (API) products to a world class standard ready for clinical development.</p>
  </section>

  <h3 class="list-label services-label">Services</h3>
  <ul class="offer-list services-list">
    <li>Bacterial / Yeast Fermentation</li>
    <li>Cell Banking</li>
    <li>Process Development/Scale-up</li>
    <li>cGMP Manufacture of<br>biopharmaceutical APIs</li>
    <li>Stability Testing</li>
  </ul>

  <h3 class="list-label products-label">Products</h3>
  <ul class="offer-list products-list">
    <li>Recombinant proteins</li>
    <li>Live Biotherapeutics</li>
    <li>Bacterial vaccines</li>
    <li>Plasmid DNA</li>
  </ul>

  <div class="brand">
    <div class="brand-name">VEROTT BIO<span class="brand-dot"></span></div>
    <div class="brand-tagline">BIOPHARMACEUTICAL MANUFACTURING</div>
  </div>

  <div class="footer-rule"></div>
  <p class="contact-line"><strong>Visit verottbio.com.au</strong><span>Australia +61(7)35550142</span><span>Email: enquiries@verottbio.com.au</span></p>
</main>
</body>
</html>
```